Improvement of design for elearning template

Our company provides web based elearning courses for employees. We have a design layout for the different slides which can be found here: https://www.filecrate-share.com/sh/qemvirt7xnoa2lup/KLpQzRtYwMbDfHsnVcEkGaUoPi?dl=0. The content will be added later. At this point we are just looking for a design layout that works with different content types like images, text, quiz & videos. What we would ask you, is to pick randomly 1 or 2 of the elearning slides from the existing designs and suggest improvements or come up with an alternative design. The winner of the design project can work on all slides and this will be a project with a much larger budget.
Target Market(s)
Employees in large enterprises
Look and feel
Each slider illustrates characteristics of the customer's brand and the style your logo design should communicate.

```html
<!DOCTYPE html>
<html lang="en">
<head>
<meta charset="utf-8">
<title>E-learning slide templates</title>
<link rel="stylesheet" href="https://fonts.googleapis.com/css2?family=Figtree:wght@400;500;600;700;800&display=swap">
<style>
:root{
  --board:#878787;
  --slide:#f8f8f9;
  --card:#ffffff;
  --line:#e4e6ec;
  --navy:#0b2a9c;
  --navy-dark:#08237f;
  --ink:#1d1d22;
  --muted:#6b6e78;
  --green:#5cc04a;
  --track:#e3e4e8;
  --tile:#f1f1f3;
  --tile-line:#d9dadf;
  --blue-1:#dbe6fb;
  --blue-2:#8eaaf0;
  --blue-3:#3e63d8;
}
*{box-sizing:border-box;margin:0;padding:0}
html,body{width:1200px;height:654px;overflow:hidden}
body{background:var(--board);font-family:"Figtree",sans-serif;color:var(--ink);position:relative}
.slide{position:absolute;width:543px;height:279px;background:var(--slide)}
.slide--welcome{left:41px;top:34px}
.slide--text{left:615px;top:34px}
.slide--quiz{left:41px;top:342px}
.slide--gallery{left:615px;top:342px}
.abs{position:absolute}
.brand{left:52px;top:15px;display:flex;align-items:center;gap:5px;color:var(--navy);font-size:9px}
.brand__mark{width:11px;height:11px;border:1.2px solid var(--navy);border-radius:50%}
.nav{left:338px;top:16px;display:flex;gap:13px;font-size:9px;color:var(--ink)}
.nav span::before{content:"";display:inline-block;width:4px;height:4px;border-right:1px solid var(--ink);border-bottom:1px solid var(--ink);transform:rotate(45deg) translateY(-3px);margin-right:5px}
.frame{left:10px;top:37px;width:523px;height:233px;background:var(--card);border:1px solid var(--line);border-radius:6px;overflow:hidden}
.progress__pct{left:62px;top:247px;font-size:6px}
.progress__track{left:20px;top:256px;width:375px;height:3px;border-radius:2px;background:var(--track)}
.progress__fill{left:20px;top:256px;width:48px;height:3px;border-radius:2px;background:var(--green)}
.progress__lesson{left:399px;top:252px;font-size:7px}
.pager{left:452px;top:251px;display:flex;align-items:center;gap:4px;font-size:7px}
.pager svg{width:12px;height:9px}
.pager .gap{width:8px}
.eyebrow{left:51px;top:54px;font-size:9.8px;color:var(--navy)}
.headline{left:51px;top:67px;font-size:12.8px;font-weight:700;color:var(--navy);white-space:nowrap}
.rule{left:52px;top:88px;width:55px;height:1px;background:var(--navy)}
.art{border-radius:40% 50% 30% 40%}
/* welcome */
.hero-art{left:60px;top:58px;width:445px;height:190px;background:radial-gradient(ellipse at 50% 60%,var(--blue-2) 0%,var(--blue-1) 55%,rgba(255,255,255,0) 75%)}
.intro-card{left:154px;top:61px;width:225px;height:141px;border:5px solid #cfdcf8;border-radius:8px;background:var(--card);text-align:center;padding-top:9px}
.intro-card__kicker{font-size:9.5px;color:var(--muted)}
.intro-card__title{font-size:15px;line-height:17px;font-weight:700;color:var(--navy);margin-top:3px}
.intro-card__body{font-size:6px;line-height:8px;text-align:left;margin:9px 13px 0;color:var(--ink)}
.btn-start{display:inline-block;margin-top:8px;width:66px;height:20px;border-radius:10px;background:var(--navy-dark);color:#fff;font-size:10px;line-height:20px}
/* text slide */
.copy{left:52px;top:105px;width:265px;font-size:7px;line-height:8.9px}
.copy p{margin-bottom:8.5px}
.copy .bullet{padding-left:4px;text-indent:-4px}
.side-art{left:346px;top:59px;width:168px;height:182px;background:linear-gradient(160deg,#a9bdf6 0%,#4f72e0 60%,#dfe7fb 100%);border-radius:18px 18px 40px 40px}
/* quiz */
.quiz-title{left:51px;top:54px;font-size:9.8px;color:var(--navy)}
.quiz-intro{left:51px;top:78px;width:400px;font-size:5px;line-height:7px;color:var(--muted)}
.quiz-intro b{font-weight:500;color:#444}
.topic{left:228px;top:102px;width:84px;height:13px;border:1px solid var(--line);border-radius:7px;font-size:7.5px;text-align:center;line-height:11px}
.question{left:70px;top:122px;width:400px;text-align:center;font-size:10.8px;line-height:14px;font-weight:500}
.options{left:92px;top:159px;width:356px;list-style:none}
.options li{height:16px;margin-bottom:2.6px;background:#f6f6f7;border-radius:8px;display:flex;align-items:center;gap:6px;padding-left:6px;font-size:8px}
.options li::before{content:"";width:8px;height:8px;border:1px solid var(--navy);border-radius:50%;flex:none}
.exam-progress{left:225px;top:237px;display:flex;align-items:center;gap:4px;font-size:5.5px;color:var(--navy)}
.dots{display:flex;gap:1.5px}
.dots i{width:2.5px;height:2.5px;border-radius:50%;background:#c6c9d4}
.dots i.on{background:var(--navy)}
/* gallery */
.tile{width:83px;height:51px;background:var(--tile);border:1px solid var(--tile-line);border-radius:2px}
.tile svg{width:100%;height:100%;display:block}
.tile-label{width:83px;text-align:center;font-size:6.3px;font-weight:600}
.tooltip{left:269px;top:123px;width:77px;height:62px;background:#fff;border-radius:5px;box-shadow:0 2px 8px rgba(0,0,0,.12);font-size:6px;line-height:8.7px;padding:7px 8px}
.tooltip::before{content:"";position:absolute;left:-9px;top:16px;border:5px solid transparent;border-right:9px solid #fff;border-left:0}
</style>
</head>
<body>

<!-- Slide: lesson start -->
<section class="slide slide--welcome">
  <div class="abs brand"><span class="brand__mark"></span>Company name</div>
  <nav class="abs nav"><span>Lessons</span><span>Menu</span><span>Glossary</span></nav>
  <div class="abs frame"></div>
  <div class="abs hero-art art" role="img" aria-label="Illustration of a desk with envelope, password bubble, laptop, shield, notebook and glasses in blue tones"></div>
  <div class="abs intro-card">
    <div class="intro-card__kicker">Lesson 1</div>
    <div class="intro-card__title">Handling sensitive<br>information</div>
    <p class="intro-card__body">Consectetur adipiscing elit, sed do eiusmod tempor incididunt ut labore et dolore magna. Excepteur sint occaecat cupidatat non proident, sunt in culpa</p>
    <span class="btn-start">Start</span>
  </div>
  <div class="abs progress__pct">10%</div>
  <div class="abs progress__track"></div><div class="abs progress__fill"></div>
  <div class="abs progress__lesson">Lesson 2</div>
  <div class="abs pager">
    <svg viewBox="0 0 12 9"><path d="M11 4.5H1.5M5 1 1.5 4.5 5 8" fill="none" stroke="#5cc04a" stroke-width="1.3"/></svg>Prev.<span class="gap"></span>Next
    <svg viewBox="0 0 12 9"><path d="M1 4.5h9.5M7 1l3.5 3.5L7 8" fill="none" stroke="#5cc04a" stroke-width="1.3"/></svg>
  </div>
</section>

<!-- Slide: text content -->
<section class="slide slide--text">
  <div class="abs brand"><span class="brand__mark"></span>Company name</div>
  <nav class="abs nav"><span>Lessons</span><span>Menu</span><span>Glossary</span></nav>
  <div class="abs frame"></div>
  <div class="abs eyebrow">Handling sensitive information</div>
  <h2 class="abs headline">Ad minim veniam, quis nostrud exerci tation</h2>
  <div class="abs rule"></div>
  <div class="abs copy">
    <p>Lorem ipsum dolor sit amet, consectetuer adipiscing elit, sed diam nonummy nibh euismod tincidunt ut lacreet dolore magna aliquam erat volupat. Ut wisi enim ad minim veniam, quis nostrud exerci tation ullamcorp</p>
    <p class="bullet">- Er suscipit lobartis nis ut aliquip Duis autem vel eum iriure Vel illum dolore eu feugiat nulla facilisis at vero</p>
    <p class="bullet">- Er suscipit lobartis nis ut aliquip Duis autem vel eum iriure Vel illum dolore eu feugiat nulla facilisis at vero</p>
    <p>Praesent luptatum zzril delerit augue duis dolore te feugait dolore te feugait nulla facilisi. Lorem ipsum dolor sit amet, cons ectetuer adipiscing elit, sed diam nonummy nibh euismod tincidunt ut laoreet dolore magna aliquam erat volutpat. Ut wisi enim ad minim veniam, quis nostrud exerci tation</p>
  </div>
  <div class="abs side-art" role="img" aria-label="Illustration of a person unlocking a large smartphone with fingerprint, card and shield icons"></div>
  <div class="abs progress__pct">10%</div>
  <div class="abs progress__track"></div><div class="abs progress__fill"></div>
  <div class="abs progress__lesson">Lesson 2</div>
  <div class="abs pager">
    <svg viewBox="0 0 12 9"><path d="M11 4.5H1.5M5 1 1.5 4.5 5 8" fill="none" stroke="#5cc04a" stroke-width="1.3"/></svg>Prev.<span class="gap"></span>Next
    <svg viewBox="0 0 12 9"><path d="M1 4.5h9.5M7 1l3.5 3.5L7 8" fill="none" stroke="#5cc04a" stroke-width="1.3"/></svg>
  </div>
</section>

<!-- Slide: quiz -->
<section class="slide slide--quiz">
  <div class="abs brand"><span class="brand__mark"></span>Company name</div>
  <nav class="abs nav"><span>Lessons</span><span>Menu</span><span>Glossary</span></nav>
  <div class="abs frame"></div>
  <div class="abs quiz-title">Phishing awareness | Exam Questions</div>
  <p class="abs quiz-intro">The exam contains <b>5 multiple choice questions. Please choose the correct answer.</b> You are only allowed to give a maximum of 3 incorrect answers, otherwise the training starts all over again.</p>
  <div class="abs topic">1. E-mail use</div>
  <p class="abs question">If you receive an e-mail with the following subject line: "Congratulations, you have won a week's holiday for two people in Italy." What do you?</p>
  <ul class="abs options">
    <li>You are curious and open the e-mail</li>
    <li>You check whether you know the sender. If not, delete the e-mail unread.</li>
    <li>You send the e-mail to the service desk</li>
    <li>You are happy about this and forward the e-mail to your partner and colleagues</li>
  </ul>
  <div class="abs exam-progress">Exam progress
    <span class="dots"><i class="on"></i><i class="on"></i><i class="on"></i><i></i><i></i><i></i><i></i><i></i><i></i><i></i><i></i><i></i><i></i></span>
  </div>
  <div class="abs progress__pct">10%</div>
  <div class="abs progress__track"></div><div class="abs progress__fill"></div>
  <div class="abs progress__lesson">Lesson 2</div>
  <div class="abs pager">
    <svg viewBox="0 0 12 9"><path d="M11 4.5H1.5M5 1 1.5 4.5 5 8" fill="none" stroke="#5cc04a" stroke-width="1.3"/></svg>Prev.<span class="gap"></span>Next
    <svg viewBox="0 0 12 9"><path d="M1 4.5h9.5M7 1l3.5 3.5L7 8" fill="none" stroke="#5cc04a" stroke-width="1.3"/></svg>
  </div>
</section>

<!-- Slide: image gallery -->
<section class="slide slide--gallery">
  <div class="abs brand"><span class="brand__mark"></span>Company name</div>
  <nav class="abs nav"><span>Lessons</span><span>Menu</span><span>Glossary</span></nav>
  <div class="abs frame"></div>
  <div class="abs eyebrow">Handling sensitive information</div>
  <h2 class="abs headline">Blandit preasent luptatum zzril delenit augue duis dolore</h2>
  <div class="abs rule"></div>

  <div class="abs tile" style="left:78px;top:102px"><svg viewBox="0 0 83 51"><circle cx="23" cy="19" r="7" fill="#e2e2e6"/><path d="M0 51 32 28 50 40 68 24 83 34V51Z" fill="#e6e6ea"/></svg></div>
  <div class="abs tile" style="left:176px;top:102px"><svg viewBox="0 0 83 51"><circle cx="23" cy="19" r="7" fill="#e2e2e6"/><path d="M0 51 32 28 50 40 68 24 83 34V51Z" fill="#e6e6ea"/></svg></div>
  <div class="abs tile" style="left:274px;top:102px"><svg viewBox="0 0 83 51"><circle cx="23" cy="19" r="7" fill="#e2e2e6"/><path d="M0 51 32 28 50 40 68 24 83 34V51Z" fill="#e6e6ea"/></svg></div>
  <div class="abs tile" style="left:373px;top:102px"><svg viewBox="0 0 83 51"><circle cx="23" cy="19" r="7" fill="#e2e2e6"/><path d="M0 51 32 28 50 40 68 24 83 34V51Z" fill="#e6e6ea"/></svg></div>
  <div class="abs tile" style="left:78px;top:175px"><svg viewBox="0 0 83 51"><circle cx="23" cy="19" r="7" fill="#e2e2e6"/><path d="M0 51 32 28 50 40 68 24 83 34V51Z" fill="#e6e6ea"/></svg></div>
  <div class="abs tile" style="left:176px;top:175px"><svg viewBox="0 0 83 51"><circle cx="23" cy="19" r="7" fill="#e2e2e6"/><path d="M0 51 32 28 50 40 68 24 83 34V51Z" fill="#e6e6ea"/></svg></div>
  <div class="abs tile" style="left:274px;top:175px"><svg viewBox="0 0 83 51"><circle cx="23" cy="19" r="7" fill="#e2e2e6"/><path d="M0 51 32 28 50 40 68 24 83 34V51Z" fill="#e6e6ea"/></svg></div>
  <div class="abs tile" style="left:373px;top:175px"><svg viewBox="0 0 83 51"><circle cx="23" cy="19" r="7" fill="#e2e2e6"/><path d="M0 51 32 28 50 40 68 24 83 34V51Z" fill="#e6e6ea"/></svg></div>

  <div class="abs tile-label" style="left:78px;top:156px">Lorem ipsum</div>
  <div class="abs tile-label" style="left:174px;top:156px">Lorem ipsum</div>
  <div class="abs tile-label" style="left:373px;top:156px">Lorem ipsum</div>
  <div class="abs tile-label" style="left:78px;top:229px">Lorem ipsum</div>
  <div class="abs tile-label" style="left:174px;top:229px">Lorem ipsum</div>
  <div class="abs tile-label" style="left:274px;top:229px">Lorem ipsum</div>
  <div class="abs tile-label" style="left:373px;top:229px">Lorem ipsum</div>

  <div class="abs tooltip">Consectetur adipiscing elit, sed do eiusmod tempor incididunt ut labore et dolore magna.</div>

  <div class="abs progress__pct">10%</div>
  <div class="abs progress__track"></div><div class="abs progress__fill"></div>
  <div class="abs progress__lesson">Lesson 2</div>
  <div class="abs pager">
    <svg viewBox="0 0 12 9"><path d="M11 4.5H1.5M5 1 1.5 4.5 5 8" fill="none" stroke="#5cc04a" stroke-width="1.3"/></svg>Prev.<span class="gap"></span>Next
    <svg viewBox="0 0 12 9"><path d="M1 4.5h9.5M7 1l3.5 3.5L7 8" fill="none" stroke="#5cc04a" stroke-width="1.3"/></svg>
  </div>
</section>

</body>
</html>
```